■ 依頼の目的/概要

私は第45回全国青葉学徒競技祭典選手権(以下、葉徒祭)運営委員会の広報局長を務めております。葉徒祭というのは、東日本と西日本から選抜された医学部学生が参加する体育大会で、開催競技は全12競技となっております。

今回は、その大会のPR用に各大学に配布するポスターのデザイン制作をお願いします。

■ 重視する点/検討基準

ポスターを見るのは主に大学医学部の学生で、一目見て葉徒祭のポスターだと分かるものがいいです。

制作する上で、必ず入れてほしいワードを以下に述べておきます。

・第45回全国青葉学徒競技祭典選手権
http://www.hatosai.kumonet.jp/top.htm(※大会HPです)
・主管:白鷺ヶ丘医療学院・浜風医療学院
・主催:北辰学徒競技協会連合・南星学徒競技協会連合
・開催競技(弓道・硬式テニス・軟式テニス・バトミントン・準硬式野球・サッカー・バスケットボール・柔道・卓球・剣道・バレーボール・ヨットの全12競技)

前年度、前々年度のポスターを添付しておりますので、ご参照下さい。

■ 利用用途

A2サイズのポスターに、片面カラーで印刷します。また、大会HPにも掲載いたします。

■ その他/注意点

データはイラストレーター形式(CS3以下)にて縦長使用でお願いします。
そのまま印刷会社に入稿するので、カラーモードはCMYKにて、塗り足し・アウトライン化もお願いします。

・ご提案を選択後に当選者様に修正を依頼する可能性がございますのでご了承下さい。
・選択させて頂いたデザインの著作権(財産権)等の扱いはMokkaro利用規約に従い、弊運営委員会に譲渡をお願いします。フォントや画像素材などを利用する場合は上記利用用途に使用できることを確認し、第三者の知的財産権等に注意して下さい。

葉徒祭につきましては下記のサイトをご参照下さい。何らかのご参考にしていただけると幸いです。また、第45回の大会HPはまだ制作しておりません。
http://www.hatosai.kumonet.jp/top.htm
http://ja.hyakkamori.jp/wiki/%E8%91%89%E5%BE%92%E7%A5%AD

以上、宜しくお願い致します。

たくさんのデザイン提案、どうもありがとうございます。
私1人だけでなく、実行委員何人かで最も相応しいと思われるものを選ばせて頂きたいと思います。
二週間位内には選びたいと思います。
■ 選んだ理由

医学生の部屋に貼っているイメージとの提案で、それが私たちのイメージにぴったりでした。また、大学に貼っていても目を引きそうなデザインでとても気に入りました。

■ 提案者全員のお礼・コメント

たくさんの提案ありがとうございました。
すばらしいものばかりだったので選ぶのに迷いましたが、委員何人かで話し合い今回はこのデザインを選ばせていただくことにしました。

```html
<!DOCTYPE html>
<html lang="ja">
<head>
<meta charset="utf-8">
<title>第45回全国青葉学徒競技祭典選手権 ポスター</title>
<link rel="stylesheet" href="https://fonts.googleapis.com/css2?family=Montserrat:wght@800&family=Noto+Sans+JP:wght@500;700;900&family=Noto+Serif:wght@700&display=swap">
<style>
:root{
  --teal:#1f9b7e;
  --teal-dark:#147a63;
  --ink:#2a2f2e;
  --paper:#ffffff;
  --sky-top:#7fa9cf;
  --sky-mid:#c6d8e8;
  --cloud:#eef1f3;
  --trees:#6f8a55;
  --grass:#8ea36a;
  --track:#a0705a;
}
*{margin:0;padding:0;box-sizing:border-box}
html,body{width:846px;height:1200px;overflow:hidden;background:var(--paper)}
.poster{position:relative;width:846px;height:1200px;background:var(--paper);font-family:"Noto Sans JP",sans-serif;color:var(--ink);overflow:hidden}
.hero-photo{position:absolute;left:0;top:0;width:846px;height:636px;
  background:
    radial-gradient(ellipse 300px 120px at 640px 190px,rgba(255,255,255,.75),rgba(255,255,255,0) 70%),
    radial-gradient(ellipse 260px 90px at 300px 330px,rgba(255,255,255,.6),rgba(255,255,255,0) 70%),
    linear-gradient(180deg,var(--sky-top) 0%,var(--sky-mid) 35%,var(--cloud) 62%,#c9d3c4 70%,var(--trees) 76%,var(--grass) 84%,var(--track) 90%,#8c5f4b 100%)}
.year{position:absolute;left:26px;top:-10px;font-family:"Montserrat",sans-serif;font-weight:800;font-size:196px;letter-spacing:22px;line-height:1;white-space:nowrap}
.year .solid{color:var(--teal)}
.year .outline{color:rgba(255,255,255,.45);-webkit-text-stroke:3px var(--teal);letter-spacing:60px}
.edition{position:absolute;left:12px;top:612px;transform-origin:left top;transform:rotate(-90deg);
  font-family:"Montserrat",sans-serif;font-weight:800;font-size:82px;color:var(--teal);line-height:1;letter-spacing:2px;white-space:nowrap}
.title{position:absolute;left:176px;top:646px;font-size:60px;font-weight:900;color:var(--teal);letter-spacing:4px;white-space:nowrap;line-height:1.2}
.title-sub{position:absolute;left:738px;top:738px;writing-mode:vertical-rl;font-size:72px;font-weight:900;color:var(--teal);letter-spacing:14px;line-height:1}
.events{position:absolute;left:34px;top:748px;width:546px}
.events-head{background:var(--teal);color:#fff;font-size:15px;font-weight:700;padding:3px 10px}
.events-list{padding:8px 4px 0 28px;font-size:18px;font-weight:700;color:var(--ink);line-height:1.65;white-space:nowrap}
.events-list span{margin-right:18px}
.credits{position:absolute;left:34px;top:990px;font-size:15px;font-weight:500;line-height:1.75;color:var(--ink);white-space:nowrap}
.credits b{color:var(--teal);font-weight:700;margin-right:10px}
.site-url{position:absolute;left:28px;top:1052px;font-family:"Noto Serif",serif;font-weight:700;font-size:37px;color:var(--teal);white-space:nowrap}
</style>
</head>
<body>
<div class="poster">
  <div class="hero-photo" role="img" aria-label="青空と雲の下、陸上トラックを並んで走る4人の学生の写真"></div>
  <div class="year"><span class="solid">20</span><span class="outline">11</span></div>
  <div class="edition">dai45kai</div>

  <h1 class="title">全国青葉学徒競技祭典</h1>
  <div class="title-sub">選手権</div>

  <section class="events">
    <div class="events-head">■開催種目</div>
    <div class="events-list">
      <div><span>弓道</span><span>硬式テニス</span><span>軟式テニス</span><span>バトミントン</span></div>
      <div><span>準硬式野球</span><span>サッカー</span><span>バスケット</span><span>柔道</span></div>
      <div><span>剣道</span><span>卓球</span><span>バレーボール</span><span>ヨット</span><span>（全12種目）</span></div>
    </div>
  </section>

  <div class="credits">
    <div><b>■主管</b>白鷺ヶ丘医療学院／浜風医療学院</div>
    <div><b>■主催</b>北辰学徒競技協会連合／南星学徒競技協会連合</div>
  </div>
  <div class="site-url">http://www.hatosai.kumonet.jp/top.htm</div>
</div>
</body>
</html>
```